Kelvaro.lu - Héritage en confiance

As a rule, most people plan everything meticulously down to the smallest detail, at least when it comes to aspects such as building a house, buying a car, or making major purchases. However, very few think about what is usually the single biggest “transaction” of their entire lives and make provisions for it. We are talking about inheritance – or, from the other perspective, inheriting. In any case, it is about estate planning.

Target Market(s)

Inheritance of a property - People that inheritated a property

Industry/Entity Type

Inheritance of a property - Real Estate

Coding

Coded - Design and coding required

Number of Pages Required

4 page

Font styles to use
Decorative

Colors
0054AA
0677BA
7BADD7
CADEEF
E8F1F8

Requirements
Must have
• Four different Navigation buttons: 1. Immobilier (if somebody inherated a house or flat) 2. Services (if people do not kow what to do) 3. Calculatrice (if people want to get an idea of the value of the house or flat) 4. Contact (to get in touch with us through a text form).
Nice to have
• Since visitors to this site may be in mourning, the website should be very user-friendly and welcoming.
Should not have
• Too bright, too many colors...

```html
<!DOCTYPE html>
<html lang="en">
<head>
<meta charset="utf-8">
<title>Kelvaro.lu – Héritage en confiance</title>
<link rel="stylesheet" href="https://fonts.googleapis.com/css2?family=Montserrat:wght@400;500;600;700&display=swap">
<style>
:root{
  --blue-deep:#0054AA;
  --blue:#0677BA;
  --blue-mid:#7BADD7;
  --blue-light:#CADEEF;
  --blue-pale:#E8F1F8;
  --ink:#1d1d1f;
  --grey:#4a4a4a;
  --white:#ffffff;
}
*{margin:0;padding:0;box-sizing:border-box}
html,body{width:1200px;height:2823px;overflow:hidden;background:var(--white)}
body{font-family:'Montserrat',sans-serif;color:var(--ink);position:relative}
.abs{position:absolute}

/* header */
.site-header{position:absolute;left:0;top:0;width:1200px;height:85px;background:var(--white)}
.brand{position:absolute;left:110px;top:24px;font-size:34px;font-weight:500;color:var(--blue);letter-spacing:.3px}
.main-nav a{position:absolute;top:34px;font-size:16px;color:#555;text-decoration:none}
.main-nav a.is-active{color:var(--blue-deep);font-weight:600;text-decoration:underline;text-underline-offset:4px}

/* hero */
.hero-visual{position:absolute;left:0;top:85px;width:1200px;height:620px}
.hero-title{position:absolute;left:111px;top:196px;color:var(--white);font-size:50px;line-height:60px;font-weight:400;letter-spacing:.5px}
.hero-title strong{font-weight:700;font-size:51px}
.hero-lead{position:absolute;left:111px;top:340px;width:400px;color:var(--white);font-size:18px;line-height:26px;text-align:justify}
.btn{position:absolute;display:flex;align-items:center;justify-content:center;border-radius:8px;font-size:16px;font-weight:500;text-decoration:none}
.btn-light{background:var(--blue-light);color:var(--ink)}
.btn-solid{background:var(--blue-deep);color:var(--white)}

/* section headings */
.section-title{position:absolute;left:0;width:1200px;text-align:center;font-size:41px;font-weight:600;color:var(--blue)}
.section-title .dark{color:var(--blue-deep)}

/* services */
.service-photo{position:absolute;top:883px;width:298px;height:303px;border-radius:12px}
.service-info{position:absolute;top:1212px;width:298px;padding-left:17px;border-left:6px solid var(--blue)}
.service-info h3{font-size:20px;font-weight:500;line-height:26px;color:var(--ink)}
.service-info p{font-size:14px;line-height:19px;color:#333;margin-top:5px;padding-left:2px}
.carousel-arrow{position:absolute;top:1008px;width:52px;height:52px;border-radius:50%;background:var(--blue-deep)}

/* calculator band */
.calc-band{position:absolute;left:0;top:1366px;width:1200px;height:204px;background:linear-gradient(100deg,#1a4fa6,#2160b6 50%,#1a55aa)}
.calc-title{position:absolute;left:109px;top:1397px;font-size:42px;font-weight:600;color:var(--white)}
.calc-text{position:absolute;left:111px;top:1483px;width:640px;font-size:15.5px;line-height:23px;color:var(--white)}

/* about */
.about-band{position:absolute;left:0;top:1570px;width:1200px;height:595px;background:var(--blue-pale)}
.about-title{position:absolute;left:632px;top:1698px;font-size:41px;font-weight:600;color:var(--blue)}
.about-text{position:absolute;left:632px;top:1785px;width:456px;font-size:14.6px;line-height:23.2px;letter-spacing:-.15px;color:#555;text-align:justify}

/* testimonials */
.review{position:absolute;top:2360px;width:297px;height:276px;border:1.5px solid #555;border-radius:12px;background:var(--white)}
.review .quote{position:absolute;left:22px;top:22px}
.review .stars{position:absolute;right:22px;top:26px;color:#f5a000;font-size:13px;letter-spacing:1px}
.review p{position:absolute;left:22px;top:76px;width:255px;font-size:12.4px;line-height:20.6px;color:#666}
.review .avatar{position:absolute;left:22px;top:204px;width:46px;height:46px;border-radius:50%;background:var(--blue-deep);color:var(--white);font-size:18px;font-weight:600;display:flex;align-items:center;justify-content:center}
.review .name{position:absolute;left:84px;top:218px;font-size:15px;color:var(--ink)}
.dot{position:absolute;top:2669px;width:10px;height:10px;border-radius:50%;background:#8a8a8a}
.dot.is-active{width:14px;height:14px;top:2667px;background:var(--blue-deep)}

/* footer */
.site-footer{position:absolute;left:0;top:2767px;width:1200px;height:56px;background:var(--blue-deep)}
.site-footer a{position:absolute;top:19px;color:var(--white);font-size:16px;text-decoration:none}
.copyright{position:absolute;right:111px;top:20px;color:var(--white);font-size:13px}
</style>
</head>
<body>

<header class="site-header">
  <div class="brand">Kelvaro</div>
  <nav class="main-nav">
    <a class="is-active" href="#" style="left:552px">Home</a>
    <a href="#" style="left:642px">About</a>
    <a href="#" style="left:731px">Services</a>
    <a href="#" style="left:834px">Calculator</a>
    <a href="#" style="left:952px">Contact</a>
    <a href="#" style="left:1054px">En
      <svg width="10" height="7" viewBox="0 0 10 7"><path d="M1 1l4 4 4-4" fill="none" stroke="#555" stroke-width="1.8"/></svg></a>
  </nav>
</header>

<svg class="hero-visual" viewBox="0 0 1200 620">
  <defs>
    <linearGradient id="heroFill" x1="0" y1="0" x2="1" y2="0.4">
      <stop offset="0" stop-color="#6b6a55"/>
      <stop offset=".35" stop-color="#4e6e2e"/>
      <stop offset=".65" stop-color="#8a8a55"/>
      <stop offset="1" stop-color="#c88b72"/>
    </linearGradient>
    <clipPath id="heroClip"><path d="M0 0H1200V485Q600 700 0 485Z"/></clipPath>
  </defs>
  <path d="M0 488Q600 700 1200 488V515Q600 690 0 515Z" fill="var(--blue-pale)"/>
  <path d="M190 545Q600 700 990 545Q600 625 190 545Z" fill="var(--blue)"/>
  <rect role="img" aria-label="Photo of a hand passing an old brass key into open palms, soft green garden behind" width="1200" height="620" fill="url(#heroFill)" clip-path="url(#heroClip)"/>
</svg>

<h1 class="hero-title">Guiding You Through<br><strong>Property Inheritance</strong></h1>
<p class="hero-lead">Clear guidance for real estate inheritance in Luxembourg, simplified.</p>
<a class="btn btn-light" href="#" style="left:112px;top:419px;width:178px;height:38px">Get Expert Advice</a>

<h2 class="section-title" style="top:772px">Our <span class="dark">Services</span></h2>
<svg class="abs" style="left:513px;top:818px" width="174" height="20" viewBox="0 0 174 20"><path d="M3 15Q80 6 170 5" fill="none" stroke="#1d1d1f" stroke-width="3.5" stroke-linecap="round"/></svg>

<div class="carousel-arrow" style="left:42px">
  <svg width="52" height="52" viewBox="0 0 52 52"><path d="M30 16L20 26l10 10" fill="none" stroke="#fff" stroke-width="3" stroke-linecap="round"/></svg>
</div>
<div class="carousel-arrow" style="left:1105px">
  <svg width="52" height="52" viewBox="0 0 52 52"><path d="M22 16l10 10-10 10" fill="none" stroke="#fff" stroke-width="3" stroke-linecap="round"/></svg>
</div>

<div class="service-photo" role="img" aria-label="Photo of an adviser reviewing documents with a young client" style="left:112px;background:linear-gradient(135deg,#6a4a36,#a88a72 55%,#d8dde4)"></div>
<div class="service-photo" role="img" aria-label="Photo of hands on a laptop with glowing house value graphics" style="left:451px;background:linear-gradient(135deg,#cfd8e0,#9fb2c2 55%,#5e6e7a)"></div>
<div class="service-photo" role="img" aria-label="Photo of a man reading paperwork at a desk" style="left:791px;background:linear-gradient(135deg,#4c5660,#8a7a52 55%,#d7dbe0)"></div>

<div class="service-info" style="left:112px"><h3>Inheritance Consultation</h3><p>Personalized advice on<br>inheritance laws &amp; real estate</p></div>
<div class="service-info" style="left:451px"><h3>Property Evaluation</h3><p>Access to professional tools &amp;<br>guidance for accurate real estate</p></div>
<div class="service-info" style="left:791px"><h3>Administrative Support</h3><p>Step-by-step assistance with legal<br>documents, tax implications</p></div>

<section class="calc-band"></section>
<h2 class="calc-title">Inheritance Calculator</h2>
<svg class="abs" style="left:110px;top:1444px" width="176" height="18" viewBox="0 0 176 18"><path d="M3 14Q80 6 172 4" fill="none" stroke="#fff" stroke-width="3.5" stroke-linecap="round"/></svg>
<p class="calc-text">Our inheritance calculator helps you estimate potential taxes, property values, and obligations quickly and easily.</p>
<a class="btn btn-light" href="#" style="left:880px;top:1448px;width:209px;height:39px">Start Calculation Now</a>

<section class="about-band"></section>
<svg class="abs" style="left:0;top:1570px" width="1200" height="595" viewBox="0 0 1200 595">
  <rect role="img" aria-label="Decorative line drawing of houses and trees" x="580" y="500" width="580" height="95" fill="var(--blue-light)" opacity=".35"/>
  <rect role="img" aria-label="Decorative dot pattern" x="1163" y="400" width="37" height="195" fill="var(--blue-mid)" opacity=".35"/>
  <path role="img" aria-label="Decorative diagonal stripe pattern" d="M72 190A160 160 0 0 1 225 80L200 65A185 185 0 0 0 72 170Z" fill="var(--blue-mid)" opacity=".5"/>
  <path d="M215 478A210 210 0 0 1 175 95" fill="none" stroke="var(--blue-deep)" stroke-width="8"/>
  <circle role="img" aria-label="Photo of two hands holding a small red house model" cx="354" cy="296" r="209" fill="#c89a82"/>
</svg>
<h2 class="about-title">About Us</h2>
<svg class="abs" style="left:631px;top:1743px" width="176" height="18" viewBox="0 0 176 18"><path d="M3 14Q80 6 172 4" fill="none" stroke="#1d1d1f" stroke-width="3.5" stroke-linecap="round"/></svg>
<p class="about-text">Kelvaro.lu is an independent platform dedicated to guiding families and individuals through real estate inheritance in Luxembourg. Our mission is to provide clear, practical, and reliable information so that you can navigate every stage of succession with confidence. With expert knowledge, transparent resources, and a focus on preserving value, we make complex legal and administrative processes easier to understand and manage.</p>
<a class="btn btn-solid" href="#" style="left:632px;top:1985px;width:130px;height:39px">Read More</a>

<h2 class="section-title" style="top:2240px">Testimonials</h2>
<svg class="abs" style="left:513px;top:2286px" width="174" height="20" viewBox="0 0 174 20"><path d="M3 15Q80 6 170 5" fill="none" stroke="#1d1d1f" stroke-width="3.5" stroke-linecap="round"/></svg>

<article class="review" style="left:107px">
  <svg class="quote" width="26" height="20" viewBox="0 0 26 20"><path d="M0 20V12Q0 3 9 0l1 3Q5 5 5 9h5v11ZM14 20V12Q14 3 23 0l1 3Q19 5 19 9h5v11Z" fill="#1d1d1f"/></svg>
  <div class="stars">★★★★★</div>
  <p>Lorem ipsum dolor sit amet, consectetur adipiscing elit, sed do eiusmod tempor incididunt ut labore et dolore magna aliqua. Quis ipsum suspendisse ultrices gravida. Risus commodo viverra maecenas accumsan</p>
  <div class="avatar">CW</div><div class="name">Claire Weber</div>
</article>
<article class="review" style="left:449px">
  <svg class="quote" width="26" height="20" viewBox="0 0 26 20"><path d="M0 20V12Q0 3 9 0l1 3Q5 5 5 9h5v11ZM14 20V12Q14 3 23 0l1 3Q19 5 19 9h5v11Z" fill="#1d1d1f"/></svg>
  <div class="stars">★★★★★</div>
  <p>Lorem ipsum dolor sit amet, consectetur adipiscing elit, sed do eiusmod tempor incididunt ut labore et dolore magna aliqua. Quis ipsum suspendisse ultrices gravida. Risus commodo viverra maecenas accumsan</p>
  <div class="avatar">CW</div><div class="name">Claire Weber</div>
</article>
<article class="review" style="left:791px">
  <svg class="quote" width="26" height="20" viewBox="0 0 26 20"><path d="M0 20V12Q0 3 9 0l1 3Q5 5 5 9h5v11ZM14 20V12Q14 3 23 0l1 3Q19 5 19 9h5v11Z" fill="#1d1d1f"/></svg>
  <div class="stars">★★★★★</div>
  <p>Lorem ipsum dolor sit amet, consectetur adipiscing elit, sed do eiusmod tempor incididunt ut labore et dolore magna aliqua. Quis ipsum suspendisse ultrices gravida. Risus commodo viverra maecenas accumsan</p>
  <div class="avatar">CW</div><div class="name">Claire Weber</div>
</article>

<span class="dot is-active" style="left:568px"></span>
<span class="dot" style="left:591px"></span>
<span class="dot" style="left:611px"></span>
<span class="dot" style="left:629px"></span>

<footer class="site-footer">
  <a href="#" style="left:111px">Home</a>
  <a href="#" style="left:199px">About</a>
  <a href="#" style="left:287px">Services</a>
  <a href="#" style="left:391px">Calculator</a>
  <a href="#" style="left:510px">Contact</a>
  <span class="copyright">© 2025 Kelvaro. All rights reserved.</span>
</footer>

</body>
</html>
```